Upsell Vertical Banner Ad Design For B2B Marketing Agency Vertical 768px × 1180px IS THE SIZE

I need a banner made for my website www.brightlanepromotionhub.biz This banner will be an upsell advertisement for after someone signs up for my monthly program. When they login to their account for the 1st time I will give them the chance to upgrade their account to our annual program with just one click.

this is a page that upsells it currently to give you an idea how we market ourselves:
https://tlpx.pagevault-example.com/page/tlp-annual-upsell

Use this content:

Are You Ready To Commit To Taking Your Business To The Next Level?

Because We're In This For The Long-Haul and Dedicated To Your Success...

Save $300 By Upgrading To An Annual Membership And Pay Only $74/mth

((BUTTON))Yes, Upgrade My Plan Right Now!

*Must prepay the full year at only $898/yr!

Target Market(s)

business owners

Industry/Entity Type

Marketing

Requirements
Must have
• 768px × 1180px IS THE SIZE vertical

Use this content:

Nice to have
• Use this content:

Should not have
• Use this content:

```html
<!DOCTYPE html>
<html lang="en">
<head>
<meta charset="utf-8">
<title>Annual Membership Upgrade</title>
<link href="https://fonts.googleapis.com/css2?family=Roboto:wght@400;500;700&family=Oswald:wght@600;700&display=swap" rel="stylesheet">
<style>
  :root {
    --green: #077537;
    --navy: #0f3866;
    --white: #ffffff;
    --ink: #111111;
  }
  * { margin: 0; padding: 0; box-sizing: border-box; }
  html, body { width: 781px; height: 1200px; overflow: hidden; background: var(--white); }
  .banner {
    position: relative;
    width: 781px;
    height: 1200px;
    font-family: "Roboto", Arial, sans-serif;
    overflow: hidden;
  }
  .headline-block {
    position: absolute; left: 0; top: 0; width: 781px; height: 504px;
    background: var(--green);
    display: flex; align-items: center; justify-content: center;
  }
  .headline {
    color: var(--white);
    font-weight: 500;
    font-size: 63px;
    line-height: 88px;
    text-align: center;
    letter-spacing: 0.5px;
    margin-top: -4px;
  }
  .offer-block {
    position: absolute; left: 0; top: 504px; width: 781px; height: 371px;
    background: var(--white);
  }
  .tagline {
    position: absolute; left: 0; top: 20px; width: 781px;
    text-align: center;
    color: var(--ink);
    font-weight: 500;
    font-size: 24.5px;
    line-height: 41px;
  }
  .savings-burst {
    position: absolute; left: 91px; top: 134px; width: 188px; height: 188px;
  }
  .savings-text {
    position: absolute; left: 91px; top: 134px; width: 188px; height: 188px;
    display: flex; flex-direction: column; align-items: center; justify-content: center;
    color: var(--white);
    font-family: "Oswald", Impact, sans-serif;
    font-weight: 700;
    text-align: center;
  }
  .savings-text .label { font-size: 40px; line-height: 44px; letter-spacing: 1px; }
  .savings-text .amount { font-size: 52px; line-height: 56px; letter-spacing: -1px; }
  .offer-copy {
    position: absolute; left: 305px; top: 150px;
    color: var(--ink);
    font-size: 33px;
    line-height: 44px;
    font-weight: 400;
  }
  .price-pill {
    position: absolute; left: 595px; top: 155px; width: 186px; height: 152px;
    background: var(--navy);
    border-radius: 76px 0 0 76px;
    color: var(--white);
    text-align: center;
    padding-left: 14px;
  }
  .price-pill .only { display: block; font-size: 27px; line-height: 28px; margin-top: 18px; font-weight: 500; }
  .price-pill .price { display: block; font-family: "Oswald", Impact, sans-serif; font-weight: 700; font-size: 60px; line-height: 62px; letter-spacing: -1px; }
  .price-pill .per { display: block; font-size: 22px; line-height: 22px; }
  .terms-band {
    position: absolute; left: 0; top: 875px; width: 781px; height: 135px;
    background: var(--navy);
    color: var(--white);
    text-align: center;
  }
  .terms-band .line-one { display: block; font-size: 43px; line-height: 50px; margin-top: 14px; font-weight: 500; }
  .terms-band .line-two { display: block; font-size: 32px; line-height: 54px; font-weight: 500; }
  .terms-band .line-two .figure {
    font-family: "Oswald", Impact, sans-serif; font-weight: 600; font-size: 42px; margin-left: 18px;
  }
  .cta-button {
    position: absolute; left: 0; top: 1010px; width: 781px; height: 190px;
    background: var(--green);
    color: var(--white);
    display: flex; align-items: center; justify-content: center;
    text-align: center;
    text-decoration: none;
    font-weight: 500;
    font-size: 70px;
    line-height: 76px;
  }
</style>
</head>
<body>
<div class="banner">
  <section class="headline-block">
    <h1 class="headline">ARE YOU READY<br>TO COMMIT TO<br>TAKING YOUR<br>BUSINESS TO<br>THE NEXT LEVEL?</h1>
  </section>

  <section class="offer-block">
    <p class="tagline">BECAUSE WE’RE IN THIS FOR THE LONG-HAUL<br>AND DEDICATED TO YOUR SUCCESS...</p>

    <svg class="savings-burst" viewBox="0 0 188 188" aria-hidden="true">
      <polygon fill="#0f3866" points="94.0,0.0 103.4,16.8 117.1,3.1 121.6,21.7 139.3,14.4 139.3,33.6 158.0,30.0 151.8,48.2 170.6,48.9 160.0,64.9 178.1,69.9 164.6,83.3 181.6,91.5 166.0,101.4 180.4,112.5 162.6,118.5 173.9,133.6 155.0,135.1 161.4,152.9 143.0,148.8 144.0,167.3 127.9,157.9 122.4,175.8 109.1,162.3 98.0,177.8 89.4,160.9 75.9,173.0 71.9,154.6 54.8,160.4 56.4,141.7 37.7,141.1 45.0,124.0 26.3,119.0 38.7,104.9 20.5,96.1 35.4,84.8 19.9,73.3 37.8,67.0 27.9,51.1 46.7,49.3 42.0,31.3 59.9,35.0 62.6,16.6 78.3,26.9 86.6,9.7"/>
    </svg>
    <div class="savings-text">
      <span class="label">SAVE</span>
      <span class="amount">$300</span>
    </div>

    <p class="offer-copy">BY UPGRADING<br>TO AN ANNUAL<br>MEMBERSHIP<br>AND PAY</p>

    <div class="price-pill">
      <span class="only">ONLY</span>
      <span class="price">$74</span>
      <span class="per">/MTH</span>
    </div>
  </section>

  <section class="terms-band">
    <span class="line-one">MUST PREPAY THE FULL YEAR</span>
    <span class="line-two">AT ONLY <span class="figure">$898</span>/YR!</span>
  </section>

  <a class="cta-button" href="https://tlpx.pagevault-example.com/page/tlp-annual-upsell">YES, UPGRADE MY<br>PLAN RIGHT NOW!</a>
</div>
</body>
</html>
```